New London based construction company website

We need a website designing for our new London based construction company which aims to provide total & brackley yard services.

The website is to have two sides to it one for "fernway yard services" and one for "brackley yard services" with an opening page with both logo's to choose from.

Would like the website to be modern, professional and inspire confidence.

Target Market(s)

Those specifically visiting the site to check that the company is professional

Industry/Entity Type

Construction

Contact Information for Business Card

One side for Brackley Yard Services the other Fernway Yard Services

Number of Pages Required

5+ page

Font styles to use
Sans Serif

Requirements
Must have
• The website is to have two sides to it one for "fernway yard services" and one for "brackley yard services" with an opening page with both logo's to choose from.

```html
<!DOCTYPE html>
<html lang="en">
<head>
<meta charset="utf-8">
<title>Fernway Yard Services</title>
<link rel="stylesheet" href="https://fonts.googleapis.com/css2?family=Cinzel:wght@400;700&family=Open+Sans:wght@400;600;700&display=swap">
<style>
:root{
  --blue:#0a66b8;
  --blue-dark:#07539a;
  --ink:#222;
  --text:#555;
  --muted:#888;
  --grey-band:#ececec;
  --faint:#e4e4e4;
  --dark:#4a4a4a;
  --darker:#333;
  --white:#fff;
}
*{margin:0;padding:0;box-sizing:border-box}
html,body{width:1200px;height:4045px;overflow:hidden;background:var(--white)}
body{position:relative;font-family:"Open Sans",Arial,sans-serif;color:var(--text)}
.abs{position:absolute}
.serif{font-family:"Cinzel",Georgia,serif}

/* header */
.site-header{left:0;top:0;width:1200px;height:94px;background:var(--white)}
.brand{left:75px;top:22px;display:flex;align-items:center;gap:14px}
.brand-mark{width:48px;height:48px;background:var(--blue)}
.brand-name{font-family:"Open Sans",Arial,sans-serif;font-weight:600;font-size:22px;color:var(--blue-dark);line-height:1}
.main-nav{right:62px;top:38px;display:flex;gap:34px;font-size:15px;color:var(--ink);text-transform:uppercase}
.nav-active-tab{left:470px;top:86px;width:54px;height:8px;background:var(--blue)}

/* hero */
.hero{left:0;top:94px;width:1200px;height:594px;background:linear-gradient(180deg,#aebfcc 0%,#7d8f9c 40%,#3a3f44 100%)}
.hero-title{left:73px;top:252px;color:var(--white);font-size:52px;line-height:56px;letter-spacing:2px}
.hero-dots{left:1124px;top:220px;display:flex;flex-direction:column;gap:7px}
.hero-dots span{width:7px;height:7px;background:var(--white);border-radius:50%}

/* connectors */
.rail{background:var(--blue)}

/* featured */
.ghost{color:var(--faint);font-size:78px;line-height:1;letter-spacing:2px}
.section-title{color:var(--ink);font-size:32px;line-height:36px;letter-spacing:1px;font-weight:700}
.body-copy{font-size:14.5px;line-height:24px;color:var(--text)}
.body-copy p+p{margin-top:22px}
.photo{display:block}
.slider-btn{width:46px;height:52px;border:1px solid #ccc;background:var(--white);display:flex;align-items:center;justify-content:center}
.btn-outline{border:2px solid var(--blue);color:var(--blue);font-weight:700;font-size:15px;display:flex;align-items:center;justify-content:center}

/* services */
.services-band{left:0;top:1375px;width:1200px;height:742px;background:var(--grey-band)}
.service-col{width:330px}
.service-col h3{font-size:14px;font-weight:700;color:var(--ink);margin-top:10px}
.service-col .rule{width:60px;height:3px;background:var(--blue);margin:10px 0 12px}
.service-col p{font-size:13.5px;line-height:22px;color:var(--muted)}

/* team */
.team-band{left:0;top:2117px;width:1200px;height:607px;background:linear-gradient(180deg,#3a3d40,#1f2123)}
.team-ghost{color:rgba(255,255,255,.22)}
.team-card{width:237px;height:351px;border:5px solid #ddd;background:#888}
.team-card .portrait{position:absolute;left:0;top:0;width:100%;height:100%}
.team-card .caption{position:absolute;left:0;bottom:0;width:100%;height:52px;background:rgba(60,60,60,.85);color:var(--white);font-weight:600;font-size:19px;display:flex;align-items:center;justify-content:center}
.team-card.is-open .caption{height:176px;background:var(--blue);flex-direction:column;justify-content:flex-start;padding:14px 16px 0}
.team-card.is-open .caption p{font-size:12.5px;line-height:17px;font-weight:400;text-align:center;margin-top:6px}
.socials{display:flex;gap:8px;margin-top:10px}
.socials span{width:27px;height:27px;border-radius:50%;background:var(--white)}

/* offer */
.offer-box{left:67px;top:2813px;width:548px;height:450px;background:var(--blue);color:var(--white)}
.offer-box h2{position:absolute;left:33px;top:34px;font-size:30px;font-weight:700;letter-spacing:1px}
.offer-item{position:absolute;width:250px;display:flex;gap:14px}
.offer-icon{width:38px;height:38px;flex:none;border:2px solid var(--white);display:flex;align-items:center;justify-content:center}
.offer-item h4{font-size:15px;font-weight:700;line-height:18px}
.offer-item p{font-size:13px;line-height:17px}
.feedback-box{left:574px;top:2939px;width:553px;height:472px;background:var(--grey-band)}
.quote-mark{font-size:80px;color:#cfcfcf;line-height:1}

/* contact */
.contact-band{left:0;top:3506px;width:1200px;height:472px;background:var(--dark);color:var(--white)}
.contact-row{display:flex;align-items:center;gap:22px;font-size:14px;line-height:19px}
.contact-icon{width:42px;height:42px;border-radius:50%;background:var(--white);display:flex;align-items:center;justify-content:center;flex:none}
.field{border:1px solid #ddd;color:var(--white);font-size:14px;padding:10px 12px}
.submit{background:#222;color:var(--white);font-size:14px;display:flex;align-items:center;justify-content:center}
.site-footer{left:0;top:3978px;width:1200px;height:67px;background:var(--darker);color:#ddd;font-size:14px;display:flex;align-items:center;justify-content:center}
</style>
</head>
<body>

<header class="abs site-header">
  <div class="abs brand"><span class="brand-mark"></span><span class="brand-name">Fernway Yard Services</span></div>
  <nav class="abs main-nav"><span>Home</span><span>About</span><span>Who are you</span><span>Service</span><span>Our work</span><span>News</span><span>Contact us</span></nav>
  <div class="abs nav-active-tab"></div>
</header>

<section class="abs hero" role="img" aria-label="Photo of cranes above a building under construction"></section>
<h1 class="abs hero-title serif">RELENTLESSLY<br>PROACTIVE..</h1>
<div class="abs hero-dots"><span></span><span></span><span></span><span></span></div>

<!-- left blue rail through featured -->
<div class="abs rail" style="left:162px;top:647px;width:54px;height:654px"></div>
<svg class="abs" style="left:162px;top:1300px" width="54" height="40" viewBox="0 0 54 40"><polygon points="0,0 54,0 54,14 27,40 0,14" fill="#0a66b8"/></svg>
<div class="abs rail" style="left:187px;top:1330px;width:4px;height:100px"></div>
<svg class="abs" style="left:176px;top:655px" width="26" height="16" viewBox="0 0 26 16"><polyline points="6,4 13,11 20,4" fill="none" stroke="#fff" stroke-width="3"/></svg>

<section>
  <div class="abs ghost serif" style="left:558px;top:742px">FEATURED</div>
  <div class="abs photo" role="img" aria-label="Hard hat and rolled blueprints on a desk" style="left:67px;top:804px;width:486px;height:356px;background:linear-gradient(135deg,#cfe0ef,#7fa7cc 55%,#d9a52a)"></div>
  <div class="abs photo" role="img" aria-label="Worker holding a yellow hard hat" style="left:359px;top:985px;width:296px;height:256px;background:linear-gradient(160deg,#8fa4b6,#2f4f7a 55%,#d8b032)"></div>
  <div class="abs slider-btn" style="left:558px;top:917px"><svg width="14" height="22"><polyline points="11,3 3,11 11,19" fill="none" stroke="#999" stroke-width="2"/></svg></div>
  <div class="abs slider-btn" style="left:605px;top:917px"><svg width="14" height="22"><polyline points="3,3 11,11 3,19" fill="none" stroke="#999" stroke-width="2"/></svg></div>
  <h2 class="abs section-title serif" style="left:701px;top:778px">FEATURED<br>PROJECTS</h2>
  <div class="abs" style="left:701px;top:864px;width:160px;height:2px;background:#bbb"></div>
  <svg class="abs" style="left:766px;top:858px" width="22" height="16"><rect x="3" y="5" width="16" height="9" fill="#0a66b8"/><rect x="7" y="1" width="8" height="5" fill="#0a66b8"/></svg>
  <div class="abs body-copy" style="left:701px;top:900px;width:420px">
    <p>Lorem Ipsum is simply dummy text of the printing and typesetting industry. Lorem Ipsum has been the industry's standard dummy text ever since the 1500s, when an unknown printer took a galley of type and scrambled it to make a type specimen book. It has survived not only five centuries,</p>
    <p>but also the leap into electronic typesetting, remaining essentially unchanged. It was popularised in the 1960s with the release of Letraset sheets containing Lorem Ipsum passages, and more recently with desktop publishing</p>
  </div>
  <div class="abs btn-outline" style="left:701px;top:1143px;width:138px;height:49px">Read More &nbsp;»</div>
</section>

<section>
  <div class="abs services-band"></div>
  <div class="abs photo" role="img" aria-label="Engineers in hard hats in front of a concrete building frame" style="left:612px;top:1340px;width:494px;height:454px;background:linear-gradient(170deg,#c9d6e2,#8a8f94 45%,#3b4c7a)"></div>
  <div class="abs ghost serif" style="left:81px;top:1456px;color:#dcdcdc">SERVICES</div>
  <h2 class="abs section-title serif" style="left:94px;top:1506px">OUR SERVICES</h2>
  <div class="abs body-copy" style="left:94px;top:1562px;width:420px">
    <p>Lorem Ipsum is simply dummy text of the printing and typesetting industry. Lorem Ipsum has been the industry's standard dummy text ever since the 1500s, when an unknown printer took a galley of type and scrambled it to make a type specimen book. It has survived not only five centuries,</p>
    <p>but also the leap into electronic typesetting, remaining essentially unchanged. It was popularised in the 1960s with the release of Letraset sheets containing Lorem Ipsum passages, and more recently with desktop publishing</p>
  </div>
  <div class="abs service-col" style="left:94px;top:1870px">
    <svg width="44" height="40"><rect x="4" y="8" width="12" height="28" fill="#0a66b8"/><rect x="16" y="16" width="24" height="20" fill="none" stroke="#0a66b8" stroke-width="3"/></svg>
    <h3>PRE-CONSTRUCTION</h3><div class="rule"></div>
    <p>Lorem Ipsum is simply dummy text of the printing and typesetting industry. Lorem Ipsum has been the industry's standard dummy text ever since the 1500s.</p>
  </div>
  <div class="abs service-col" style="left:440px;top:1870px">
    <svg width="44" height="40"><rect x="4" y="28" width="36" height="8" fill="#0a66b8"/><rect x="10" y="18" width="24" height="8" fill="#0a66b8"/><rect x="16" y="8" width="12" height="8" fill="#0a66b8"/></svg>
    <h3>CONSTRUCTION PHASE</h3><div class="rule"></div>
    <p>Lorem Ipsum is simply dummy text of the printing and typesetting industry. Lorem Ipsum has been the industry's standard dummy text ever since the 1500s.</p>
  </div>
  <div class="abs service-col" style="left:790px;top:1870px">
    <svg width="44" height="40"><rect x="4" y="6" width="34" height="22" fill="none" stroke="#0a66b8" stroke-width="3"/><rect x="16" y="28" width="10" height="8" fill="#0a66b8"/></svg>
    <h3>POST-CONTRUCTION</h3><div class="rule"></div>
    <p>Lorem Ipsum is simply dummy text of the printing and typesetting industry. Lorem Ipsum has been the industry's standard dummy text ever since the 1500s.</p>
  </div>
</section>

<section>
  <div class="abs team-band" role="img" aria-label="Dark construction site backdrop"></div>
  <div class="abs rail" style="left:980px;top:2077px;width:4px;height:160px"></div>
  <div class="abs ghost serif team-ghost" style="left:67px;top:2157px">TEAM</div>
  <h2 class="abs section-title serif" style="left:100px;top:2196px;color:#fff">OUR TEAM</h2>
  <div class="abs team-card is-open" style="left:67px;top:2292px">
    <div class="portrait" role="img" aria-label="Portrait of a smiling team member" style="background:linear-gradient(180deg,#c9a46a,#3d6aa8)"></div>
    <div class="caption">Sam Keller<p>Lorem Ipsum is simply dummy text of the printing and typesetting industry. Lorem Ipsum has been the industry</p><div class="socials"><span></span><span></span><span></span><span></span><span></span></div></div>
  </div>
  <div class="abs team-card" style="left:343px;top:2292px">
    <div class="portrait" role="img" aria-label="Portrait of a worker in a hard hat and safety vest" style="background:linear-gradient(180deg,#e0a52b,#6d5a48 45%,#c9d64a)"></div>
    <div class="caption">Sam Keller</div>
  </div>
  <div class="abs team-card" style="left:618px;top:2292px">
    <div class="portrait" role="img" aria-label="Portrait of a carpenter at a workbench" style="background:linear-gradient(180deg,#d8d8d8,#7a6a5a 55%,#b08d64)"></div>
    <div class="caption">Sam Keller</div>
  </div>
  <div class="abs team-card" style="left:893px;top:2292px">
    <div class="portrait" role="img" aria-label="Portrait of a smiling worker in a yellow hard hat" style="background:linear-gradient(180deg,#e6cf33,#c7b39a 45%,#9aa3ab)"></div>
    <div class="caption">Sam Keller</div>
  </div>
</section>

<section>
  <div class="abs ghost serif" style="left:431px;top:2764px;color:#eee">PRINCIPAL</div>
  <div class="abs rail" style="left:998px;top:2724px;width:4px;height:148px"></div>
  <svg class="abs" style="left:971px;top:2866px" width="60" height="73" viewBox="0 0 60 73"><polygon points="30,0 60,20 60,73 0,73 0,20" fill="#0a66b8"/></svg>
  <div class="abs feedback-box"></div>
  <svg class="abs" style="left:971px;top:3411px" width="60" height="68" viewBox="0 0 60 68"><polygon points="0,0 60,0 60,50 30,68 0,50" fill="#0a66b8"/></svg>
  <div class="abs rail" style="left:998px;top:3470px;width:4px;height:118px"></div>

  <div class="abs offer-box">
    <h2 class="serif">WHAT WE OFFER?</h2>
    <div class="offer-item" style="left:22px;top:104px"><span class="offer-icon"><svg width="20" height="20"><rect x="2" y="8" width="16" height="10" fill="#fff"/></svg></span><div><h4>Construction</h4><p>Lorem Ipsum dolor sit amet consectetur adipiscing</p></div></div>
    <div class="offer-item" style="left:289px;top:104px"><span class="offer-icon"><svg width="20" height="20"><circle cx="10" cy="10" r="6" fill="#fff"/></svg></span><div><h4>Awesome Stuff</h4><p>Lorem Ipsum dolor sit amet consectetur adipiscing</p></div></div>
    <div class="offer-item" style="left:22px;top:212px"><span class="offer-icon"><svg width="20" height="20"><circle cx="10" cy="10" r="6" fill="none" stroke="#fff" stroke-width="3"/></svg></span><div><h4>Maintanance</h4><p>Lorem Ipsum dolor sit amet consectetur adipiscing</p></div></div>
    <div class="offer-item" style="left:289px;top:212px"><span class="offer-icon"><svg width="20" height="20"><circle cx="10" cy="10" r="6" fill="none" stroke="#fff" stroke-width="3"/></svg></span><div><h4>Maintanance</h4><p>Lorem Ipsum dolor sit amet consectetur adipiscing</p></div></div>
    <div class="offer-item" style="left:22px;top:320px"><span class="offer-icon"><svg width="20" height="20"><rect x="3" y="3" width="14" height="14" fill="none" stroke="#fff" stroke-width="3"/></svg></span><div><h4>Good Planning</h4><p>Lorem Ipsum dolor sit amet consectetur adipiscing</p></div></div>
    <div class="offer-item" style="left:289px;top:320px"><span class="offer-icon"><svg width="20" height="20"><rect x="3" y="3" width="14" height="14" fill="none" stroke="#fff" stroke-width="3"/></svg></span><div><h4>Good Planning</h4><p>Lorem Ipsum dolor sit amet consectetur adipiscing</p></div></div>
  </div>

  <h2 class="abs section-title serif" style="left:655px;top:2982px">COUSTOMER<br>FEEDBACK</h2>
  <div class="abs quote-mark serif" style="left:655px;top:3060px">“</div>
  <p class="abs body-copy" style="left:655px;top:3084px;width:420px">Lorem Ipsum is simply dummy text of the printing and typesetting industry. Lorem Ipsum has been the industry's standard dummy text ever since the 1500s.Lorem Ipsum is simply dummy text of the printing and typesetting industry. Lorem Ipsum has been the industry's standard dummy text ever since the 1500s.</p>
  <div class="abs" style="left:780px;top:3270px;width:304px;text-align:right">
    <div style="color:var(--blue);font-weight:700;font-size:14px">Ellis Warne</div>
    <div style="font-size:13.5px;line-height:22px;color:var(--muted);margin-top:6px">Was. Our multiply winged divided, him Saw darkness make be whales don't and land fifth great</div>
  </div>
</section>

<section class="abs contact-band">
  <h2 class="abs serif" style="left:84px;top:80px;font-size:36px;letter-spacing:1px">GET IN TOUCH</h2>
  <p class="abs" style="left:84px;top:132px;width:560px;font-size:14px;line-height:19px">We are very approachable and would love to speak to you. Feel free to call, send us an email, Tweet us or simply complete the enquiry form.</p>
  <div class="abs contact-row" style="left:79px;top:205px"><span class="contact-icon"><svg width="18" height="22"><path d="M9 1a7 7 0 0 1 7 7c0 5-7 13-7 13S2 13 2 8a7 7 0 0 1 7-7z" fill="#4a4a4a"/><circle cx="9" cy="8" r="2.5" fill="#fff"/></svg></span><span>Eastford, Northvale, offering services<br>Northvale wide</span></div>
  <div class="abs contact-row" style="left:79px;top:273px"><span class="contact-icon"><svg width="22" height="16"><rect x="1" y="1" width="20" height="14" fill="none" stroke="#4a4a4a" stroke-width="2"/><polyline points="1,1 11,9 21,1" fill="none" stroke="#4a4a4a" stroke-width="2"/></svg></span><span>info@fernwayyard.com</span></div>
  <div class="abs contact-row" style="left:79px;top:343px"><span class="contact-icon"><svg width="20" height="20"><path d="M4 2l4 4-2 3c1 2 3 4 5 5l3-2 4 4-2 3C9 19 1 11 1 4z" fill="#4a4a4a"/></svg></span><span>+44 xxxxxxxxxxxxx</span></div>
  <div class="abs field" style="left:494px;top:216px;width:264px;height:43px">Name</div>
  <div class="abs field" style="left:494px;top:270px;width:264px;height:43px">Number</div>
  <div class="abs field" style="left:494px;top:326px;width:264px;height:43px">Mail</div>
  <div class="abs field" style="left:779px;top:216px;width:340px;height:153px">Message</div>
  <div class="abs submit" style="left:494px;top:383px;width:113px;height:43px">SUBMIT</div>
</section>

<footer class="abs site-footer">All rights reserved Copyright © 2017 Fernway Yard Services</footer>

</body>
</html>
```